I need a business Card Design for my practice , i am clinical herbalist. I am a herbalist specializing in Lyme disease, autism, autoimmune diseases, difficult to cure diseasesDifficult to cure diseases. In my innovative practice i link traditional medicine, herbs with science, immunologu ,pharmacology.

Industry/Entity Type

Business

Contact Information for Business Card

My company name : OŚRODEK ZIELNIK
My name : Piotr Kaleta
Name of my profession : Fitoterapeuta
In Polish language Fitoterapeuta is Herbalist .

e-mail: piotrkaleta@osrodekzielnik.com
www.osrodek-zielnik.pl
phone : 604 587 231
My company adress : Dąbrowa Sitnicka 41 , 38-415 Lużna
I dont have logo .

Requirements
Nice to have
• My company

```html
<!DOCTYPE html>
<html lang="pl">
<head>
<meta charset="utf-8">
<title>Ośrodek Zielnik – wizytówka</title>
<link rel="stylesheet" href="https://fonts.googleapis.com/css2?family=Cinzel:wght@400;600&family=Montserrat:wght@400;500;600&display=swap">
<style>
  :root {
    --leaf: #55803a;
    --leaf-deep: #4a7331;
    --lime: #8ab833;
    --paper: #ffffff;
    --stage: #3a3a3a;
  }
  * { box-sizing: border-box; margin: 0; padding: 0; }
  html, body { width: 1200px; height: 864px; overflow: hidden; }
  body {
    background: var(--stage);
    position: relative;
    font-family: "Montserrat", Arial, sans-serif;
  }
  .card {
    position: absolute;
    left: 280px;
    width: 640px;
    height: 366px;
    border-radius: 24px;
    overflow: hidden;
    box-shadow: 0 12px 28px rgba(0,0,0,.45);
  }
  .card--front { top: 36px; background: var(--leaf); color: var(--paper); }
  .card--back { top: 462px; background: var(--paper); }

  .brand {
    font-family: "Cinzel", "Times New Roman", serif;
    font-weight: 400;
    letter-spacing: 1px;
    white-space: nowrap;
  }
  .card--front .brand {
    position: absolute;
    top: 150px; left: 0; right: 0;
    text-align: center;
    font-size: 46px;
  }
  .card--front .site {
    position: absolute;
    bottom: 34px; left: 0; right: 0;
    text-align: center;
    font-size: 13px;
    letter-spacing: .3px;
  }

  .back-shape { position: absolute; inset: 0; }
  .card--back .brand {
    position: absolute;
    top: 42px; right: 40px;
    font-size: 38px;
    color: var(--leaf);
    font-weight: 600;
  }
  .contact {
    position: absolute;
    left: 44px; top: 196px;
    color: var(--paper);
  }
  .contact__name { font-size: 22px; font-weight: 600; line-height: 1.1; }
  .contact__role { font-size: 14px; line-height: 1.2; margin-bottom: 8px; }
  .contact__company { font-size: 14px; font-weight: 600; letter-spacing: .3px; line-height: 1.15; }
  .contact__address { font-size: 14px; line-height: 1.2; margin-bottom: 8px; }
  .contact__row { display: flex; align-items: center; gap: 9px; font-size: 14px; line-height: 1.3; }
  .contact__row svg { width: 14px; height: 14px; flex: none; }
</style>
</head>
<body>

<section class="card card--front">
  <h1 class="brand">Ośrodek Zielnik</h1>
  <p class="site">www.osrodek-zielnik.pl</p>
</section>

<section class="card card--back">
  <svg class="back-shape" viewBox="0 0 640 366" aria-hidden="true">
    <path d="M0 190 Q 300 120 640 124 L640 366 L0 366 Z" fill="var(--leaf)"/>
    <path d="M250 142 Q 450 104 640 100 L640 118 Q 450 114 250 142 Z" fill="var(--lime)"/>
    <path d="M240 146 Q 450 112 640 120" fill="none" stroke="#fff" stroke-width="2"/>
  </svg>
  <h2 class="brand">Ośrodek Zielnik</h2>

  <div class="contact">
    <p class="contact__name">Piotr Kaleta</p>
    <p class="contact__role">Fitoterapeuta</p>
    <p class="contact__company">OŚRODEK ZIELNIK</p>
    <p class="contact__address">Dąbrowa Sitnicka 41, 38-415 Lużna</p>
    <p class="contact__row">
      <svg viewBox="0 0 16 16"><path d="M4 1.5 6.2 4.3 4.9 6a8 8 0 0 0 5.1 5.1l1.7-1.3 2.8 2.2-1.6 2.3C7.4 14.6 1.4 8.6 1.7 3.1Z" fill="#fff"/></svg>
      604 587 231
    </p>
    <p class="contact__row">
      <svg viewBox="0 0 16 16"><rect x="1" y="3.5" width="14" height="9.5" fill="#fff"/><path d="M1 3.5 8 9l7-5.5" fill="none" stroke="var(--leaf)" stroke-width="1.3"/></svg>
      piotrkaleta@osrodekzielnik.com
    </p>
    <p class="contact__row">
      <svg viewBox="0 0 16 16" fill="none" stroke="#fff" stroke-width="1.3"><circle cx="8" cy="8" r="6.5"/><ellipse cx="8" cy="8" rx="2.8" ry="6.5"/><path d="M1.5 8h13M2.6 4.6h10.8M2.6 11.4h10.8"/></svg>
      www.osrodek-zielnik.pl
    </p>
  </div>
</section>

</body>
</html>
```